Rear Window Advertisement and Magnets for side doors

Questions about Solvanta insurance?
Ask me, I'm a nurse
629-###-####
(Disclaimer.................in small print....)

```html
<!DOCTYPE html>
<html lang="en">
<head>
<meta charset="utf-8">
<title>Solvanta Insurance Door Magnet</title>
<link href="https://fonts.googleapis.com/css2?family=Montserrat:wght@400;700&display=swap" rel="stylesheet">
<style>
  :root {
    --page-bg: #f2f3f5;
    --magnet-top: #3d7fe8;
    --magnet-bottom: #16b0f0;
    --magnet-border: #d8345f;
    --text-white: #ffffff;
    --cross-outline: #d8345f;
  }
  html, body {
    margin: 0;
    padding: 0;
    overflow: hidden;
  }
  body {
    width: 1200px;
    height: 720px;
    background: var(--page-bg);
    position: relative;
    font-family: "Montserrat", sans-serif;
  }
  .door-magnet {
    position: absolute;
    left: 180px;
    top: 158px;
    width: 840px;
    height: 402px;
    box-sizing: border-box;
    border: 7px solid var(--magnet-border);
    background: linear-gradient(180deg, var(--magnet-top) 0%, var(--magnet-bottom) 100%);
    color: var(--text-white);
    padding: 26px 0 0 36px;
  }
  .magnet-headline {
    margin: 0;
    font-size: 50px;
    line-height: 64px;
    font-weight: 400;
    letter-spacing: 0.2px;
  }
  .magnet-headline strong {
    font-weight: 700;
  }
  .headline-line {
    display: block;
    white-space: nowrap;
  }
  .magnet-phone {
    margin: 18px 0 0;
    font-size: 92px;
    line-height: 1;
    font-weight: 700;
    letter-spacing: 0.5px;
    white-space: nowrap;
  }
  .medical-cross {
    position: absolute;
    left: 724px;
    top: 122px;
    width: 150px;
    height: 150px;
  }
</style>
</head>
<body>
  <div class="door-magnet">
    <h1 class="magnet-headline">
      <span class="headline-line"><strong>QUESTIONS</strong> ABOUT</span>
      <span class="headline-line"><strong>SOLVANTA INSURANCE?</strong></span>
      <span class="headline-line">ASK ME, <strong>I'M A NURSE</strong></span>
    </h1>
    <p class="magnet-phone">629-418-2057</p>
    <svg class="medical-cross" viewBox="0 0 150 150" aria-hidden="true">
      <path d="M58 14 H92 V58 H136 V92 H92 V136 H58 V92 H14 V58 H58 Z"
            fill="var(--text-white)" stroke="var(--cross-outline)" stroke-width="7" stroke-linejoin="miter"/>
    </svg>
  </div>
</body>
</html>
```